Crust Harbor Hotel Coupon

Would like to design a coupon that is for hotels' staff and to be dropped off at the hotel front office anytime someone calls from a hotel and as a Thank You for hotel staff for recommending us. Coupon value to be $ 2.00. Should say Thank You or Thank you for recommending us. Need our phone number 250 614 3750 on it. Color scheme to be Green and Red as in the attached logo. Coupon to be designed for printing size 3.5 inches high and 7.5 inches wide. Rear should say Fastest Delivery, Favourite Pizza for Sports teams etc. Ask for group deals. Attached logo to be on the coupon. Coupon should say coupon # and space left for us write number

```html
<!DOCTYPE html>
<html lang="en">
<head>
<meta charset="utf-8">
<title>Crust Harbor – Thank You Coupon</title>
<link href="https://fonts.googleapis.com/css2?family=Lobster&family=Teko:wght@400;500;600&display=swap" rel="stylesheet">
<style>
  :root {
    --page: #ece7e1;
    --red-top: #e20b18;
    --red-bottom: #b30d13;
    --green: #1f9a3e;
    --white: #ffffff;
    --ink: #1b1b1b;
  }
  html, body {
    margin: 0;
    width: 1200px;
    height: 693px;
    overflow: hidden;
    background: var(--page);
  }
  .coupon {
    position: absolute;
    left: 30px;
    top: 71px;
    width: 1140px;
    height: 550px;
    overflow: hidden;
    box-shadow: 0 6px 18px rgba(0,0,0,0.18);
  }
  .coupon-shapes {
    position: absolute;
    inset: 0;
  }
  .brand {
    position: absolute;
    left: 46px;
    top: 58px;
    width: 250px;
    height: 110px;
    display: flex;
    align-items: center;
    gap: 10px;
    font-family: "Teko", sans-serif;
    font-weight: 600;
    font-size: 46px;
    line-height: 1;
    color: var(--white);
    white-space: nowrap;
  }
  .brand-dot {
    flex: none;
    width: 20px;
    height: 20px;
    border-radius: 50%;
    background: var(--green);
    margin-top: -6px;
  }
  .coupon-number {
    position: absolute;
    left: 346px;
    top: 81px;
    width: 219px;
    height: 52px;
    background: var(--white);
    border-radius: 7px;
    box-sizing: border-box;
    padding-left: 14px;
    font-family: "Teko", sans-serif;
    font-size: 32px;
    line-height: 56px;
    color: var(--ink);
  }
  .thanks {
    position: absolute;
    left: 114px;
    top: 218px;
    color: var(--white);
    font-family: "Lobster", cursive;
    white-space: nowrap;
  }
  .thanks-title {
    display: block;
    font-size: 76px;
    line-height: 1;
  }
  .thanks-sub {
    display: block;
    margin-top: -8px;
    margin-left: 2px;
    font-size: 38px;
    line-height: 1.1;
    transform: rotate(-2deg);
    transform-origin: left center;
  }
  .value-badge {
    position: absolute;
    left: 488px;
    top: 179px;
    width: 204px;
    height: 204px;
    border-radius: 50%;
    background: var(--green);
    box-sizing: border-box;
    border: 6px solid var(--white);
    color: var(--white);
    font-family: "Teko", sans-serif;
    text-align: center;
  }
  .value-amount {
    display: block;
    margin-top: 30px;
    font-size: 84px;
    font-weight: 500;
    line-height: 0.85;
  }
  .value-label {
    display: block;
    font-size: 40px;
    line-height: 1;
  }
  .pitch {
    position: absolute;
    left: 55px;
    top: 377px;
    margin: 0;
    color: var(--white);
    font-family: "Teko", sans-serif;
    font-weight: 400;
    font-size: 28px;
    line-height: 34px;
    white-space: nowrap;
  }
  .order {
    position: absolute;
    left: 50px;
    top: 460px;
    display: flex;
    align-items: center;
    gap: 14px;
    color: var(--white);
    font-family: "Teko", sans-serif;
    font-weight: 600;
    font-style: italic;
    font-size: 54px;
    line-height: 1;
    letter-spacing: 1px;
    white-space: nowrap;
  }
  .order-phone-icon {
    width: 36px;
    height: 36px;
    margin-top: -8px;
  }
</style>
</head>
<body>
  <main class="coupon">
    <svg class="coupon-shapes" width="1140" height="550" viewBox="0 0 1140 550">
      <defs>
        <linearGradient id="redFill" x1="0" y1="0" x2="0" y2="1">
          <stop offset="0" stop-color="#e20b18"/>
          <stop offset="1" stop-color="#b30d13"/>
        </linearGradient>
        <radialGradient id="pizzaFill" cx="0.55" cy="0.5" r="0.6">
          <stop offset="0" stop-color="#d9a060"/>
          <stop offset="0.55" stop-color="#c0743d"/>
          <stop offset="0.8" stop-color="#5a3a2c"/>
          <stop offset="1" stop-color="#1d2631"/>
        </radialGradient>
      </defs>
      <rect class="card-base" width="1140" height="550" fill="url(#redFill)"/>
      <path class="photo-edge" d="M720 0 Q425 275 720 550 L1140 550 L1140 0 Z" fill="#1f9a3e"/>
      <path class="photo-area" role="img" aria-label="Photo of a sliced vegetable pizza with peppers, olives and onion on a dark board"
            d="M740 0 Q455 275 740 550 L1140 550 L1140 0 Z" fill="url(#pizzaFill)"/>
      <path class="ribbon" d="M45 204 L560 204 L560 349 L45 349 L84 276 Z" fill="#1f9a3e"/>
    </svg>

    <div class="brand"><span class="brand-dot"></span>Crust Harbor</div>

    <div class="coupon-number">#</div>

    <div class="thanks">
      <span class="thanks-title">Thank You</span>
      <span class="thanks-sub">for recommending us</span>
    </div>

    <div class="value-badge">
      <span class="value-amount">$2.00</span>
      <span class="value-label">VALUE</span>
    </div>

    <p class="pitch">FASTEST DELIVERY, FAVOURITE PIZZA FOR SPORTS TEAMS ETC.<br>ASK FOR GROUP DEALS.</p>

    <div class="order">
      <span class="order-label">ORDER NOW</span>
      <svg class="order-phone-icon" viewBox="0 0 36 36" aria-hidden="true">
        <circle cx="18" cy="18" r="16" fill="none" stroke="#ffffff" stroke-width="2.5"/>
        <path d="M12.5 10.5 L15.5 10 L17 14 L15 15.6 C16 18 18 20 20.4 21 L22 19 L26 20.5 L25.5 23.5 C24.5 25 22 25.5 19 24 C15 22 12 19 11 15 C10.5 13 11 11.5 12.5 10.5 Z" fill="#ffffff"/>
      </svg>
      <span class="order-number">250 614 3750</span>
    </div>
  </main>
</body>
</html>
```